Packaging design for handmade soap

We are looking for a packaging design for a brand new product line: handmade soaps, called VELMO

We are looking for a design of an outer box together with the logo. We need the design for a 90x65x30mm box (see attached). We trying to get a high-end product preferable with vintage elements (but we don't want a shiny box, it will be finished with matte lacque, however logo or other certain elements could be shiny).

The design should reflect the fact that we have a handmade, all natural soap.

I uploaded a couple of packaging examples I like.

UPDATE 1: It also should have a title, which describes the product more accurate, like "Natural Soap with Seabuckthorn and Olive oil"

UPDATE 2: I would remove the expression "high-end" from the description if high end would mean a lot of flowers in the background. I would like if you would insist about the ideea of "natural" in your works

UPDATE 3: Prefered colors green and brown (which brings the ideea of nature, natural)

Target Market(s)

Women 20-45 years with above average income

Industry/Entity Type

Cosmetics

Font styles to use
Serif

Colors
9bcb3c
acd036
cadf82
f78f20
ffc214
f37122
fbed22
fece3e
faa54b

Requirements
Must have
• A literal representation of the brand VELMO (we don't have a logo for it)

```html
<!DOCTYPE html>
<html lang="en">
<head>
<meta charset="utf-8">
<title>VELMO Handmade Soap Packaging</title>
<link href="https://fonts.googleapis.com/css2?family=Quicksand:wght@500;600;700&display=swap" rel="stylesheet">
<style>
  :root {
    --page: #e9ebea;
    --olive-dark: #1f9a45;
    --olive-band: #5bb85b;
    --olive-wash-a: #d9ead9;
    --olive-wash-b: #a9d2b4;
    --olive-wash-c: #eef4ec;
    --camomile-dark: #e3213f;
    --camomile-band: #ef6a65;
    --camomile-wash-a: #f9dede;
    --camomile-wash-b: #f2aab0;
    --camomile-wash-c: #fbeeea;
    --label-white: #f8f8f6;
    --ink-light: #ffffff;
  }
  * { margin: 0; padding: 0; box-sizing: border-box; }
  html, body { width: 824px; height: 1200px; overflow: hidden; background: var(--page); }
  body { font-family: "Quicksand", sans-serif; position: relative; }
  .box-front { position: absolute; left: 56px; width: 712px; height: 514px; }
  .box-front--olive { top: 76px; }
  .box-front--camomile { top: 636px; }
  .box-front svg { display: block; width: 100%; height: 100%; }
  .brand-name { font-family: "Quicksand", sans-serif; font-weight: 700; font-size: 76px; letter-spacing: 4px; }
  .brand-tagline { font-family: "Quicksand", sans-serif; font-weight: 600; font-size: 22px; }
  .variant-name { font-family: "Quicksand", sans-serif; font-weight: 700; font-size: 58px; fill: var(--ink-light); }
  .variant-benefit { font-family: "Quicksand", sans-serif; font-weight: 600; font-size: 22px; fill: var(--ink-light); }
  .olive .brand-name, .olive .brand-tagline { fill: var(--olive-dark); }
  .camomile .brand-name, .camomile .brand-tagline { fill: var(--camomile-dark); }
</style>
</head>
<body>

<div class="box-front box-front--olive">
  <svg class="olive" viewBox="0 0 710 512" xmlns="http://www.w3.org/2000/svg">
    <defs>
      <linearGradient id="olive-wash" x1="0" y1="0" x2="1" y2="1">
        <stop offset="0" stop-color="var(--olive-wash-c)"/>
        <stop offset="0.35" stop-color="var(--olive-wash-a)"/>
        <stop offset="0.7" stop-color="var(--olive-wash-c)"/>
        <stop offset="1" stop-color="var(--olive-wash-b)"/>
      </linearGradient>
      <path id="label-shape" d="M62 200 C62 160 100 150 110 130 L110 110 C140 110 160 95 170 80 C230 80 260 36 355 36 C450 36 480 80 540 80 C550 95 570 110 600 110 L600 130 C610 150 666 160 666 200 L666 330 C666 370 610 380 600 400 L600 420 C570 420 550 435 540 450 C480 450 450 476 355 476 C260 476 230 450 170 450 C160 435 140 420 110 420 L110 400 C100 380 62 370 62 330 Z"/>
      <clipPath id="olive-label-clip"><use href="#label-shape"/></clipPath>
    </defs>
    <rect class="box-artwork" width="710" height="512" fill="url(#olive-wash)" role="img" aria-label="Watercolour wash with line-drawn olive branches and olives"/>
    <g class="label">
      <use href="#label-shape" fill="var(--label-white)"/>
      <rect x="0" y="270" width="710" height="242" fill="var(--olive-band)" clip-path="url(#olive-label-clip)"/>
      <use href="#label-shape" fill="none" stroke="var(--olive-dark)" stroke-width="10"/>
      <use href="#label-shape" fill="none" stroke="var(--olive-band)" stroke-width="2" stroke-dasharray="1 5" stroke-linecap="round" transform="translate(355 256) scale(0.94) translate(-355 -256)"/>
    </g>
    <text class="brand-name" x="355" y="202" text-anchor="middle">VELMO</text>
    <text class="brand-tagline" x="355" y="232" text-anchor="middle">Natural Handmade Soap</text>
    <text class="variant-name" x="355" y="340" text-anchor="middle">olive oil</text>
    <text class="variant-benefit" x="355" y="378" text-anchor="middle">Superior Moisturizing</text>
  </svg>
</div>

<div class="box-front box-front--camomile">
  <svg class="camomile" viewBox="0 0 710 512" xmlns="http://www.w3.org/2000/svg">
    <defs>
      <linearGradient id="camomile-wash" x1="0" y1="0" x2="1" y2="1">
        <stop offset="0" stop-color="var(--camomile-wash-c)"/>
        <stop offset="0.3" stop-color="var(--camomile-wash-b)"/>
        <stop offset="0.65" stop-color="var(--camomile-wash-a)"/>
        <stop offset="1" stop-color="var(--camomile-wash-b)"/>
      </linearGradient>
      <path id="label-shape-b" d="M62 200 C62 160 100 150 110 130 L110 110 C140 110 160 95 170 80 C230 80 260 36 355 36 C450 36 480 80 540 80 C550 95 570 110 600 110 L600 130 C610 150 666 160 666 200 L666 330 C666 370 610 380 600 400 L600 420 C570 420 550 435 540 450 C480 450 450 476 355 476 C260 476 230 450 170 450 C160 435 140 420 110 420 L110 400 C100 380 62 370 62 330 Z"/>
      <clipPath id="camomile-label-clip"><use href="#label-shape-b"/></clipPath>
    </defs>
    <rect class="box-artwork" width="710" height="512" fill="url(#camomile-wash)" role="img" aria-label="Watercolour wash with line-drawn camomile flowers"/>
    <g class="label">
      <use href="#label-shape-b" fill="var(--label-white)"/>
      <rect x="0" y="270" width="710" height="242" fill="var(--camomile-band)" clip-path="url(#camomile-label-clip)"/>
      <use href="#label-shape-b" fill="none" stroke="var(--camomile-dark)" stroke-width="10"/>
      <use href="#label-shape-b" fill="none" stroke="var(--camomile-band)" stroke-width="2" stroke-dasharray="1 5" stroke-linecap="round" transform="translate(355 256) scale(0.94) translate(-355 -256)"/>
    </g>
    <text class="brand-name" x="355" y="202" text-anchor="middle">VELMO</text>
    <text class="brand-tagline" x="355" y="232" text-anchor="middle">Natural Handmade Soap</text>
    <text class="variant-name" x="355" y="340" text-anchor="middle">camomile</text>
    <text class="variant-benefit" x="355" y="378" text-anchor="middle">Balance &amp; Mild</text>
  </svg>
</div>

</body>
</html>
```